Brookvane Holdings Ltd - Logo and Business Card

Create a logo and business card design for our new company.

Canadian private investment company with holdings in Saskatchewan Oil and real-estate.

Target Market(s)

Investors

Industry/Entity Type

Finance

Contact Information for Business Card

Logo
Name - Dalton Pryce
Position - President
Phone - 306.482.7159
Website - www.brookvaneholdings.ca

Logo Text

Today. Tomorrow. Together. (Tag Line)

Colors

Designer to choose colors to be used in the design.

Requirements
Must have
• Logo Must Have - Type Font only
• Must be modern, professional and stand out from the crowd.
Nice to have
• Don't have any, blank slate.

```html
<!DOCTYPE html>
<html lang="en">
<head>
<meta charset="utf-8">
<title>Brookvane Holdings Ltd — Business Card</title>
<link href="https://fonts.googleapis.com/css2?family=Open+Sans:wght@300;400;600;700&display=swap" rel="stylesheet">
<style>
  :root {
    --backdrop: #d9d6d2;
    --card: #0b0b0b;
    --card-edge: #1c1c1c;
    --divider: #1f1f1f;
    --green-light: #8cc63f;
    --green-mid: #4fa83d;
    --green-dark: #2e8b3e;
    --white: #f2f2f2;
    --silver: #c9c9c9;
  }
  * { box-sizing: border-box; margin: 0; padding: 0; }
  html, body {
    width: 1200px; height: 900px; overflow: hidden;
    background: var(--backdrop);
    font-family: "Open Sans", Arial, sans-serif;
  }
  .canvas {
    position: relative; width: 1200px; height: 900px;
    display: flex; align-items: center; justify-content: center; gap: 60px;
  }
  .card {
    position: relative; width: 525px; height: 300px;
    background: var(--card);
    border: 1px solid var(--card-edge);
    box-shadow: 0 10px 30px rgba(0,0,0,.25);
    overflow: hidden;
  }
  /* Front */
  .card--front .brand-zone {
    position: absolute; left: 0; top: 0; width: 240px; height: 100%;
    display: flex; align-items: center; justify-content: center; gap: 10px;
  }
  .brand-square { width: 14px; height: 14px; background: var(--green-mid); }
  .brand-name--green {
    color: var(--green-mid); font-weight: 600; font-size: 17px; line-height: 1.2;
    width: 130px;
  }
  .card--front .divider {
    position: absolute; left: 240px; top: 60px; bottom: 60px;
    width: 1px; background: var(--divider);
  }
  .contact {
    position: absolute; left: 270px; top: 92px;
  }
  .contact__name { font-weight: 700; font-size: 19px; line-height: 1.1; }
  .contact__first { color: var(--green-light); }
  .contact__last { color: var(--green-mid); }
  .contact__title { color: var(--white); font-size: 13px; margin-top: 3px; }
  .contact__list { list-style: none; margin-top: 34px; }
  .contact__item {
    display: flex; align-items: center; gap: 8px;
    color: var(--white); font-size: 14px; line-height: 1.6;
  }
  .contact__icon { width: 11px; height: 11px; flex: none; }
  /* Back */
  .card--back {
    display: flex; align-items: center; justify-content: center;
  }
  .brand-name--silver {
    color: var(--silver); font-weight: 300; font-size: 30px;
    letter-spacing: 3px; text-align: center; line-height: 1.3;
  }
</style>
</head>
<body>
  <main class="canvas">
    <section class="card card--front" aria-label="Business card front">
      <div class="brand-zone">
        <span class="brand-square" aria-hidden="true"></span>
        <span class="brand-name--green">Brookvane Holdings Ltd</span>
      </div>
      <div class="divider"></div>
      <div class="contact">
        <p class="contact__name"><span class="contact__first">Dalton</span> <span class="contact__last">Pryce</span></p>
        <p class="contact__title">President</p>
        <ul class="contact__list">
          <li class="contact__item">
            <svg class="contact__icon" viewBox="0 0 24 24" aria-hidden="true"><path fill="#8cc63f" d="M6.6 10.8a15.1 15.1 0 0 0 6.6 6.6l2.2-2.2c.3-.3.7-.4 1-.2 1.1.4 2.3.6 3.6.6.6 0 1 .4 1 1V20c0 .6-.4 1-1 1A17 17 0 0 1 3 4c0-.6.4-1 1-1h3.5c.6 0 1 .4 1 1 0 1.3.2 2.5.6 3.6.1.3 0 .7-.2 1z"/></svg>
            306.482.7159
          </li>
          <li class="contact__item">
            <svg class="contact__icon" viewBox="0 0 24 24" aria-hidden="true"><circle cx="12" cy="12" r="10" fill="none" stroke="#8cc63f" stroke-width="3"/><path d="M2 12h20M12 2c3 3 3 17 0 20M12 2c-3 3-3 17 0 20" fill="none" stroke="#8cc63f" stroke-width="2"/></svg>
            www.brookvaneholdings.ca
          </li>
        </ul>
      </div>
    </section>
    <section class="card card--back" aria-label="Business card back">
      <p class="brand-name--silver">Brookvane Holdings Ltd</p>
    </section>
  </main>
</body>
</html>
```